Website for Trayvora.net - a web site to market and sell our online school lunch ordering system.

We need a web site to market and engage our online school lunch ordering software. Caterers all over United States are looking for a software that helps them grow by replacing paper based systems with online ordering systems that parents can use to place lunch orders for their kids. Our mobile app compliments our web app by giving parents the freedom to order when they are not in front of their computers or at home. We would like to see designs that can engage our prospects by telling a compelling story about our product with features, metrics, product tours and screenshots.

```html
<!DOCTYPE html>
<html lang="en">
<head>
<meta charset="utf-8">
<title>Trayvora – Online School Lunch Ordering</title>
<link href="https://fonts.googleapis.com/css2?family=Poppins:wght@400;500;600;700&display=swap" rel="stylesheet">
<style>
:root{
  --crimson:#b3002e;
  --crimson-dark:#6c0b2c;
  --plum:#4b0a2c;
  --ink:#222;
  --muted:#555;
  --light:#ececec;
  --white:#fff;
  --black:#0c0c0c;
}
*{box-sizing:border-box;margin:0;padding:0}
html,body{width:1200px;height:4009px;overflow:hidden}
body{position:relative;font-family:'Poppins',sans-serif;color:var(--ink);background:var(--white)}
.abs{position:absolute}
.btn{position:absolute;display:flex;align-items:center;justify-content:center;border-radius:24px;font-weight:600;font-size:15px}

/* hero */
.hero{left:0;top:0;width:1200px;height:716px;background:linear-gradient(110deg,#2c2c2e 0%,#5b5856 45%,#3a3837 70%,#1d1d1f 100%)}
.hero-shade{left:0;top:0;width:1200px;height:716px;background:rgba(0,0,0,.38)}
.burger{left:88px;top:36px;width:28px}
.burger span{display:block;height:4px;background:var(--white);margin-bottom:5px;border-radius:2px}
.nav{right:88px;top:34px;display:flex;gap:42px;color:var(--white);font-size:16px;font-weight:500}
.dots{left:72px;top:330px}
.dots i{display:block;width:9px;height:9px;border-radius:50%;background:var(--white);margin-bottom:9px}
.dots b{display:block;width:1px;height:30px;background:rgba(255,255,255,.6);margin-left:4px}
.hero-title{left:0;width:1200px;top:262px;text-align:center;color:var(--white);font-size:44px;font-weight:700}
.hero-sub{left:0;width:1200px;top:326px;text-align:center;color:var(--white);font-size:29px;font-weight:600}
.hero-text{left:200px;width:800px;top:384px;text-align:center;color:var(--white);font-size:17px;line-height:27px}
.hero .btn,.hero-btn{left:485px;top:470px;width:230px;height:44px;background:var(--crimson);color:var(--white)}

/* why */
.phone-art{left:160px;top:866px;width:300px;height:364px;border-radius:40px 40px 0 140px;background:linear-gradient(160deg,#e9e9ec,#c8c3c2 60%,#b79c90);z-index:2}
.why-title{left:567px;top:794px;font-size:36px;font-weight:700;color:var(--crimson)}
.why-list{left:574px;top:858px;width:520px;list-style:none;font-size:16px;line-height:26px;color:var(--ink)}
.why-list li{position:relative;padding-left:30px;margin-bottom:4px}
.why-list li svg{position:absolute;left:0;top:5px}
.why-list .sub{padding-left:0;color:var(--crimson);font-weight:700;font-size:18px;margin:8px 0 4px}
.why-btn{left:572px;top:1096px;width:208px;height:48px;background:var(--crimson-dark);color:var(--white)}

/* product band */
.band{left:0;top:1140px;width:1200px;height:650px}
.product-title{left:90px;top:1330px;font-size:36px;font-weight:700;color:var(--white)}
.product-text{left:90px;top:1400px;width:560px;font-size:15px;line-height:26px;color:var(--white)}
.product-btn{left:90px;top:1590px;width:208px;height:48px;background:var(--white);color:var(--crimson)}
.monitor-screen{left:690px;top:1282px;width:410px;height:290px;border:10px solid #1e1e22;border-radius:6px;background:linear-gradient(135deg,#3b3fd0,#5a5ff0 60%,#2d2fa8)}
.monitor-neck{left:850px;top:1572px;width:70px;height:36px;background:#c9c9cc}
.monitor-base{left:770px;top:1606px;width:230px;height:12px;border-radius:6px;background:#dcdcdf}

/* features */
.features{left:0;top:1778px;width:1200px;height:538px;background:var(--light)}
.sec-title{left:0;width:1200px;text-align:center;font-size:36px;font-weight:700;color:var(--crimson)}
.sec-text{left:300px;width:600px;text-align:center;font-size:15px;line-height:26px;color:var(--ink)}
.card{top:1935px;width:300px;height:265px;border:2px solid #9a9a9a;background:var(--white);display:flex;flex-direction:column;align-items:center;padding-top:50px;font-size:17px;color:#333}
.card.active{background:var(--crimson);border-color:var(--crimson);color:var(--white)}
.card svg{margin-bottom:36px}
.pager{left:0;width:1200px;top:2212px;display:flex;justify-content:center;align-items:center;gap:60px;font-size:15px}
.pager .prev{color:#333}
.pager .next{color:var(--crimson)}
.pager .pips i{display:inline-block;width:10px;height:10px;border-radius:50%;background:#333;margin:0 2px}
.pager .pips i:first-child{background:var(--crimson)}

/* audience */
.audience{left:0;top:2315px;width:1200px;height:386px;background:linear-gradient(90deg,#a5002c 0%,#c41a45 50%,#a5002c 100%)}
.aud-left{left:0;top:2315px;width:600px;height:386px;background:linear-gradient(180deg,rgba(60,0,15,.25),rgba(0,0,0,0))}
.aud-title{top:2382px;font-size:36px;font-weight:700;color:var(--white)}
.aud-text{top:2440px;width:440px;font-size:15px;line-height:26px;color:var(--white)}
.aud-more{top:2616px;font-size:17px;font-weight:600;color:var(--white)}

/* pricing */
.plan{background:var(--light);box-shadow:0 6px 18px rgba(0,0,0,.12);text-align:center}
.plan h3{font-size:25px;font-weight:700;color:var(--crimson);margin-top:42px}
.plan .rate{font-size:16px;line-height:26px;margin-top:8px;color:#333}
.plan hr{border:0;border-top:2px solid var(--crimson);width:200px;margin:30px auto 20px}
.plan ul{list-style:none;display:inline-block;text-align:left;font-size:16px;line-height:30px}
.plan ul li{padding-left:26px;position:relative}
.plan ul li svg{position:absolute;left:0;top:8px}
.plan .order{display:block;margin:0 auto;width:100px;height:32px;line-height:32px;border-radius:16px;background:var(--crimson-dark);color:var(--white);font-size:14px;font-weight:600}
.plan.pro{background:var(--crimson);color:var(--white);box-shadow:none}
.plan.pro h3,.plan.pro .rate{color:var(--white)}
.plan.pro hr{border-color:rgba(255,255,255,.8)}
.plan.pro .order{background:var(--white);color:var(--crimson);width:110px;height:36px;line-height:36px;border-radius:18px}

/* stats */
.stats{left:0;top:3408px;width:1200px;height:220px;background:var(--crimson)}
.stat{top:3445px;width:300px;text-align:center;color:var(--white)}
.stat .label{font-size:17px;font-weight:600;margin-top:14px}
.stat .num{font-size:28px;font-weight:700;margin-top:6px}

/* footer */
.footer{left:0;top:3627px;width:1200px;height:382px;background:var(--black);color:var(--white)}
.f-head{top:3670px;font-size:19px;font-weight:600;color:var(--white)}
.f-links{left:86px;top:3716px;list-style:none;font-size:14px;line-height:24px;color:var(--white)}
.social{left:86px;top:3846px;display:flex;gap:10px}
.social i{width:12px;height:12px;border-radius:50%;background:var(--white);display:block}
.f-contact{left:361px;top:3710px;font-size:14px;line-height:22px;color:var(--white)}
.f-contact .row{position:relative;padding-left:28px;margin-bottom:14px}
.f-contact svg{position:absolute;left:0;top:3px}
.field{position:absolute;background:var(--white);color:#444;font-size:12px;padding:6px 10px}
.submit{left:700px;top:3905px;width:161px;height:34px;background:var(--crimson-dark);color:var(--white);font-size:13px;font-weight:600;display:flex;align-items:center;justify-content:center}
.copy{left:0;width:1200px;top:3970px;text-align:center;font-size:12px;color:#ccc}
</style>
</head>
<body>

<!-- hero -->
<section class="abs hero" role="img" aria-label="Photo of a businesswoman holding a tablet at a meeting table"></section>
<div class="abs hero-shade"></div>
<div class="abs burger"><span></span><span></span><span></span></div>
<nav class="abs nav"><span>Pricing</span><span>Product Features</span><span>Request a Demo</span><span>Contact Us</span></nav>
<div class="abs dots"><i></i><i></i><b></b></div>
<h1 class="abs hero-title">Trayvora</h1>
<p class="abs hero-sub">Order Online Your Food</p>
<p class="abs hero-text">Sed ut perspiciatis unde omnis iste natus error sit voluptatem accusantium doloremque laudantium, totam rem aperiam, eaque ipsa quae ab illo</p>
<a class="btn hero-btn">Contact Us</a>

<!-- why -->
<div class="abs phone-art" role="img" aria-label="Hand holding a smartphone showing the Trayvora app"></div>
<h2 class="abs why-title">Why TV is better</h2>
<ul class="abs why-list">
  <li><svg width="18" height="16" viewBox="0 0 18 16"><path d="M1 9l5 5L17 1" fill="none" stroke="#b3002e" stroke-width="3"/></svg>Modern UI for end users (end customers)</li>
  <li><svg width="18" height="16" viewBox="0 0 18 16"><path d="M1 9l5 5L17 1" fill="none" stroke="#b3002e" stroke-width="3"/></svg>Mobile App: Most of our competitors do not have an installable app for iOS and</li>
  <li class="sub">Android.</li>
  <li><svg width="18" height="16" viewBox="0 0 18 16"><path d="M1 9l5 5L17 1" fill="none" stroke="#b3002e" stroke-width="3"/></svg>Advanced Menu Builder with advanced concepts like Master Menu Templates</li>
  <li><svg width="18" height="16" viewBox="0 0 18 16"><path d="M1 9l5 5L17 1" fill="none" stroke="#b3002e" stroke-width="3"/></svg>Analytics offering Business insights for caterers.</li>
</ul>
<a class="btn why-btn">Download The App</a>

<!-- product band -->
<svg class="abs band" width="1200" height="650" viewBox="0 0 1200 650">
  <defs><linearGradient id="bandGrad" x1="0" y1="0" x2="1" y2="0"><stop offset="0" stop-color="#4b0a2c"/><stop offset="1" stop-color="#b8002f"/></linearGradient></defs>
  <polygon points="0,95 1200,9 1200,485 0,638" fill="url(#bandGrad)"/>
</svg>
<h2 class="abs product-title">Product</h2>
<p class="abs product-text">Sed ut perspiciatis unde omnis iste natus error sit voluptatem accusantium doloremque laudantium, totam rem aperiam, eaque ipsa quae ab illo inventore veritatis et quasi architecto beatae vitae dicta sunt explicabo. Nemo enim ipsam voluptatem quia voluptas sit aspernatur aut odit aut fugit, sed quia consequuntur magni dolores eos qui ratione voluptatem sequi nesciunt.</p>
<a class="btn product-btn">Download The App</a>
<div class="abs monitor-screen" role="img" aria-label="Illustration of online food delivery on a desktop screen"></div>
<div class="abs monitor-neck"></div>
<div class="abs monitor-base"></div>

<!-- features -->
<section class="abs features"></section>
<h2 class="abs sec-title" style="top:1780px">Features</h2>
<p class="abs sec-text" style="top:1836px">Sed ut perspiciatis unde omnis iste natus error sit voluptatem accusantium doloremque laudantium, totam rem aperiamsunt explicabo.</p>
<div class="abs card" style="left:102px">
  <svg width="110" height="110" viewBox="0 0 110 110" fill="none" stroke="#222" stroke-width="4"><path d="M55 6l11 10 15-3 4 14 14 6-4 14 8 12-12 9 1 15-15 2-7 13-14-7-14 7-7-13-15-2 1-15-12-9 8-12-4-14 14-6 4-14 15 3z"/><circle cx="42" cy="42" r="7"/><circle cx="68" cy="68" r="7"/><path d="M72 36L38 74"/></svg>
  Flexible Pricing
</div>
<div class="abs card active" style="left:436px">
  <svg width="110" height="110" viewBox="0 0 110 110" fill="none" stroke="#fff" stroke-width="4"><path d="M20 36h70l-6 66H26z"/><path d="M38 36V26a17 17 0 0 1 34 0v10"/><path d="M40 70l10 10 20-20"/></svg>
  Automated Ordering
</div>
<div class="abs card" style="left:770px">
  <svg width="110" height="110" viewBox="0 0 110 110" fill="none" stroke="#222" stroke-width="4"><rect x="30" y="6" width="50" height="98" rx="8"/><path d="M30 20h50M30 88h50"/><circle cx="55" cy="96" r="3"/><path d="M42 46h26l-3 24H45z"/><path d="M48 46v-5a7 7 0 0 1 14 0v5"/></svg>
  Mobile App
</div>
<div class="abs pager"><span class="prev">⟵ Previous</span><span class="pips"><i></i><i></i><i></i></span><span class="next">Next ⟶</span></div>

<!-- audience -->
<section class="abs audience" role="img" aria-label="Crimson tinted photos of caterers and school cafeteria"></section>
<div class="abs aud-left"></div>
<h2 class="abs aud-title" style="left:86px">Caterers</h2>
<p class="abs aud-text" style="left:86px">Sed ut perspiciatis unde omnis iste natus error sit voluptatem accusantium doloremque laudantium, totam rem aperiam, eaque ipsa quae ab illo inventore veritatis et quasi architecto beatae vitae dicta sunt explicabo. Nemo enim ipsam voluptatem quia voluptas sit aspernatur aut odit aut fugit</p>
<span class="abs aud-more" style="left:86px">Read More</span>
<h2 class="abs aud-title" style="right:88px">Schools</h2>
<p class="abs aud-text" style="right:88px;text-align:right">Sed ut perspiciatis unde omnis iste natus error sit voluptatem accusantium doloremque laudantium, totam rem aperiam, eaque ipsa quae ab illo inventore veritatis et quasi architecto beatae vitae dicta sunt explicabo. Nemo enim ipsam voluptatem quia voluptas sit aspernatur aut odit aut fugit</p>
<span class="abs aud-more" style="right:88px">Read More</span>

<!-- pricing -->
<h2 class="abs sec-title" style="top:2745px">Pricing</h2>
<p class="abs sec-text" style="top:2803px;left:260px;width:680px">At vero eos et accusamus et iusto odio dignissimos ducimus qui blanditiis praesentium voluptatum deleniti atque corrupti quos dolores et</p>

<div class="abs plan" style="left:115px;top:2900px;width:313px;height:388px">
  <h3>Basic</h3>
  <p class="rate">( 8 cents per meal -<br>less than 10k meals per month)</p>
  <hr>
  <ul>
    <li><svg width="16" height="14" viewBox="0 0 18 16"><path d="M1 9l5 5L17 1" fill="none" stroke="#b3002e" stroke-width="3"/></svg>At vero eos et</li>
    <li><svg width="16" height="14" viewBox="0 0 18 16"><path d="M1 9l5 5L17 1" fill="none" stroke="#b3002e" stroke-width="3"/></svg>At vero eos et</li>
    <li><svg width="16" height="14" viewBox="0 0 18 16"><path d="M1 9l5 5L17 1" fill="none" stroke="#b3002e" stroke-width="3"/></svg>At vero eos et</li>
    <li><svg width="16" height="14" viewBox="0 0 18 16"><path d="M1 9l5 5L17 1" fill="none" stroke="#b3002e" stroke-width="3"/></svg>At vero eos et</li>
  </ul>
  <hr style="margin-top:16px">
  <span class="order">Order</span>
</div>

<div class="abs plan pro" style="left:444px;top:2881px;width:337px;height:428px">
  <h3>Pro</h3>
  <p class="rate" style="font-size:18px;line-height:30px">( 6 cents per meal -<br>10 to 50k meals per month)</p>
  <hr>
  <ul style="font-size:17px;line-height:32px">
    <li><svg width="16" height="14" viewBox="0 0 18 16"><path d="M1 9l5 5L17 1" fill="none" stroke="#fff" stroke-width="3"/></svg>At vero eos et</li>
    <li><svg width="16" height="14" viewBox="0 0 18 16"><path d="M1 9l5 5L17 1" fill="none" stroke="#fff" stroke-width="3"/></svg>At vero eos et</li>
    <li><svg width="16" height="14" viewBox="0 0 18 16"><path d="M1 9l5 5L17 1" fill="none" stroke="#fff" stroke-width="3"/></svg>At vero eos et</li>
    <li><svg width="16" height="14" viewBox="0 0 18 16"><path d="M1 9l5 5L17 1" fill="none" stroke="#fff" stroke-width="3"/></svg>At vero eos et</li>
  </ul>
  <hr style="margin-top:16px">
  <span class="order">Order</span>
</div>

<div class="abs plan" style="left:802px;top:2900px;width:307px;height:388px">
  <h3>Enterprise</h3>
  <p class="rate">( 4.5 cents per meal -<br>more than 50k meal per month)</p>
  <hr>
  <ul>
    <li><svg width="16" height="14" viewBox="0 0 18 16"><path d="M1 9l5 5L17 1" fill="none" stroke="#b3002e" stroke-width="3"/></svg>At vero eos et</li>
    <li><svg width="16" height="14" viewBox="0 0 18 16"><path d="M1 9l5 5L17 1" fill="none" stroke="#b3002e" stroke-width="3"/></svg>At vero eos et</li>
    <li><svg width="16" height="14" viewBox="0 0 18 16"><path d="M1 9l5 5L17 1" fill="none" stroke="#b3002e" stroke-width="3"/></svg>At vero eos et</li>
    <li><svg width="16" height="14" viewBox="0 0 18 16"><path d="M1 9l5 5L17 1" fill="none" stroke="#b3002e" stroke-width="3"/></svg>At vero eos et</li>
  </ul>
  <hr style="margin-top:16px">
  <span class="order">Order</span>
</div>

<!-- stats -->
<section class="abs stats"></section>
<div class="abs stat" style="left:95px">
  <svg width="80" height="76" viewBox="0 0 80 76" fill="none" stroke="#fff" stroke-width="3"><rect x="8" y="4" width="42" height="56" rx="3"/><path d="M16 16h26M16 26h26M16 36h18"/><circle cx="56" cy="50" r="18"/><path d="M48 50l6 6 10-12"/></svg>
  <p class="label">Orders Served</p><p class="num">300K +</p>
</div>
<div class="abs stat" style="left:450px">
  <svg width="80" height="76" viewBox="0 0 80 76" fill="none" stroke="#fff" stroke-width="3"><path d="M8 50a32 32 0 0 1 64 0z"/><path d="M4 56h72"/><circle cx="40" cy="14" r="4"/><path d="M26 8l-4-4M54 8l4-4M40 2V0"/><path d="M20 64c8 6 32 6 40 0"/></svg>
  <p class="label">Meals Served</p><p class="num">1.5 million +</p>
</div>
<div class="abs stat" style="left:765px">
  <svg width="80" height="76" viewBox="0 0 80 76" fill="none" stroke="#fff" stroke-width="3"><path d="M40 4v14M40 4h12v7H40"/><path d="M24 34l16-16 16 16"/><rect x="24" y="34" width="32" height="38"/><rect x="6" y="44" width="18" height="28"/><rect x="56" y="44" width="18" height="28"/><path d="M35 72V58h10v14"/><circle cx="40" cy="44" r="5"/></svg>
  <p class="label">Schools/ Camps</p><p class="num">1000 +</p>
</div>

<!-- footer -->
<footer class="abs footer"></footer>
<h4 class="abs f-head" style="left:86px">Links</h4>
<ul class="abs f-links"><li>Pricing</li><li>Product Features</li><li>Request a Demo</li><li>Contact Us</li></ul>
<div class="abs social"><i></i><i></i><i></i><i></i></div>

<h4 class="abs f-head" style="left:361px">Contact Us</h4>
<div class="abs f-contact">
  <div class="row"><svg width="14" height="18" viewBox="0 0 14 18"><path d="M7 0a7 7 0 0 0-7 7c0 5 7 11 7 11s7-6 7-11a7 7 0 0 0-7-7z" fill="#fff"/><circle cx="7" cy="7" r="2.5" fill="#0c0c0c"/></svg>Trayvora<br>215 Larkspur Lane # 120<br>Fairmont, CA 94512</div>
  <div class="row"><svg width="16" height="16" viewBox="0 0 16 16"><path d="M3 1l3 3-2 2c1 2 3 4 5 5l2-2 3 3-2 3C6 15 1 10 0 3z" fill="#fff"/></svg>555 014 2290</div>
</div>

<h4 class="abs f-head" style="left:700px">Request A Quote</h4>
<div class="field" style="left:700px;top:3721px;width:203px;height:32px">Name</div>
<div class="field" style="left:907px;top:3721px;width:200px;height:32px">Email</div>
<div class="field" style="left:700px;top:3764px;width:407px;height:32px">Phone Number</div>
<div class="field" style="left:700px;top:3804px;width:407px;height:85px">Message</div>
<div class="abs submit">Submit</div>
<p class="abs copy">© 2018 Copyrights | All Rights Reserved</p>

</body>
</html>
```